Website for Painting Company

Hi,
We are after a Wordpress website design with CSS/HTML Theme for our painting company based in Brisbane, Australia. Our business name is Felix Morrow Painting Contractors and we have been trading for 33 years.
We want a website that is modern and fresh with a professional image. Our organisation does Commercial, Residential and Insurance Painting projects. I have listed a couple of similar websites that we like the look and feel of. These are a guide only and we are happy to see you own designs with a similar professional image.
http://www.kelbrookcoatings.com.au/
http://www.tidewellfinishes.com.au/
We are a member of Guild Decorators Australia and I have supplied the logo named "gda" which I have included in the files I have uploaded.
We want a five page site. These are Home Page, Residential, Commercial, Insurance and Contact Us.
I have also uploaded our logo and some pictures labeled Logo,Residential, Commercial, Insurance and Homepage. These should be used on each page listed above.
Updates
Project Deadline Extended
Reason: We are extending because we need more time to go through the designs and give feedback. There are many fantastic designs. Thank you everyone who has contributed!!!!
All the best
Derek
Industry/Entity Type
Painting
Requirements
Must have
- We want a five page site. These are Home Page, Residential, Commercial, Insurance and Contact Us.

```html
<!DOCTYPE html>
<html lang="en">
<head>
<meta charset="utf-8">
<title>Felix Morrow Painting Contractors</title>
<link rel="stylesheet" href="https://fonts.googleapis.com/css2?family=Ubuntu:wght@400;500&display=swap">
<style>
  :root {
    --red: #e1222b;
    --text: #3d3d3d;
    --body-text: #454545;
    --band: #e3e3e3;
    --footer: #e0e0e0;
    --white: #ffffff;
    --rule: #6a6a6a;
  }
  * { box-sizing: border-box; margin: 0; padding: 0; }
  html, body { width: 1200px; height: 1090px; overflow: hidden; }
  body {
    position: relative;
    background: var(--white);
    font-family: "Ubuntu", sans-serif;
    color: var(--text);
  }

  .brand {
    position: absolute; left: 130px; top: 30px;
    display: flex; align-items: flex-start; gap: 10px;
    color: var(--red); font-size: 22px; font-weight: 500; line-height: 26px;
  }
  .brand-mark { width: 14px; height: 14px; background: var(--red); margin-top: 6px; }

  .main-nav {
    position: absolute; top: 84px; left: 398px;
    display: flex; height: 38px; align-items: center;
  }
  .main-nav a {
    position: relative; display: block; height: 38px; line-height: 38px;
    font-size: 17.5px; color: var(--text); text-decoration: none;
    padding: 0 19px; margin-right: 0;
  }
  .main-nav a.is-active { background: var(--red); color: var(--white); padding: 0 20px; margin-right: 0; }
  .main-nav a.is-active::after {
    content: ""; position: absolute; left: 50%; bottom: -9px; margin-left: -8px;
    border-left: 8px solid transparent; border-right: 8px solid transparent;
    border-top: 9px solid var(--red);
  }

  .hero-band { position: absolute; left: 0; top: 125px; width: 1200px; height: 344px; background: var(--band); }
  .hero-shadow {
    position: absolute; left: 176px; top: 484px; width: 855px; height: 32px;
    background: radial-gradient(ellipse at 50% 0%, rgba(0,0,0,.42), rgba(0,0,0,0) 70%);
  }
  .hero-slide {
    position: absolute; left: 129px; top: 149px; width: 942px; height: 335px;
    border: 3px solid var(--white); border-radius: 6px;
    background: linear-gradient(100deg, #cfc5b8 0%, #ebe6df 30%, #f4f2ee 55%, #d9d4cb 75%, #9fb58a 90%, #c9c4bb 100%);
    box-shadow: 0 0 2px rgba(0,0,0,.25);
  }
  .slide-dots { position: absolute; right: 8px; bottom: 6px; display: flex; gap: 4px; }
  .slide-dots span { width: 12px; height: 12px; border-radius: 50%; background: #f0f0f0; border: 1px solid #888; }
  .slide-dots span.is-current { background: #b3161c; border-color: #700; }

  .services-title {
    position: absolute; left: 130px; top: 552px;
    font-size: 23px; font-weight: 500; color: var(--text); letter-spacing: .3px;
  }
  .services-rule {
    position: absolute; left: 130px; top: 582px; width: 920px; height: 1px;
    background: linear-gradient(90deg, var(--rule) 80%, rgba(106,106,106,0));
  }

  .service-card { position: absolute; top: 604px; width: 280px; height: 326px; }
  .service-card::before {
    content: ""; position: absolute; inset: 0 0 auto 0; height: 130px;
    border: 1.5px solid var(--red); border-bottom: none; border-radius: 20px 20px 0 0;
    background: linear-gradient(#f6f6f6, rgba(255,255,255,0));
    -webkit-mask-image: linear-gradient(#000 30%, transparent);
    mask-image: linear-gradient(#000 30%, transparent);
  }
  .service-card h3 {
    position: relative; text-align: center; font-weight: 400; font-size: 18.5px;
    color: var(--red); padding-top: 10px; letter-spacing: .3px;
  }
  .service-photo {
    position: absolute; left: 22px; top: 37px; width: 236px; height: 157px;
    border: 1px solid #666;
  }
  .service-card p {
    position: absolute; left: 24px; top: 200px; width: 230px;
    font-size: 13.2px; line-height: 20px; color: var(--body-text);
  }
  .read-more {
    position: absolute; right: 24px; top: 303px;
    font-size: 13.2px; color: var(--red); text-decoration: none;
  }
  .card-residential { left: 130px; }
  .card-commercial { left: 461px; }
  .card-insurance { left: 790px; }
  .photo-residential { background: linear-gradient(#5d9be0 0%, #a9cdf0 45%, #c9c3b6 70%, #5f8a3f 100%); }
  .photo-commercial { background: linear-gradient(#3e72c4 0%, #8db0e0 40%, #d9dadd 60%, #9a8f7e 100%); }
  .photo-insurance { background: linear-gradient(#4f8fd6 0%, #a6c7ec 40%, #e5e5e5 65%, #6e9a46 100%); }

  .site-footer { position: absolute; left: 0; top: 940px; width: 1200px; height: 150px; background: var(--footer); border-top: 1px solid #d0d0d0; }
  .member-label {
    position: absolute; left: 139px; top: 18px;
    font-size: 10.5px; font-weight: 500; font-style: normal; color: #1a3fa8;
  }
  .member-badge {
    position: absolute; left: 160px; top: 40px; width: 80px; height: 62px;
    background: #2f55c4; border-radius: 8px;
  }
  .copyright {
    position: absolute; right: 131px; top: 24px;
    font-size: 12.5px; color: var(--text);
  }
</style>
</head>
<body>
  <header>
    <div class="brand"><span class="brand-mark"></span><span>Felix Morrow<br>Painting Contractors</span></div>
    <nav class="main-nav">
      <a href="#" class="is-active">HOME</a>
      <a href="#">RESIDENTIAL</a>
      <a href="#">COMMERCIAL</a>
      <a href="#">INSURANCE</a>
      <a href="#">CONTACT US</a>
    </nav>
  </header>

  <div class="hero-band"></div>
  <div class="hero-shadow"></div>
  <div class="hero-slide" role="img" aria-label="Bright open-plan living and dining room with white floors, cream sofas and a garden view">
    <div class="slide-dots"><span></span><span></span><span class="is-current"></span></div>
  </div>

  <h2 class="services-title">OUR SERVICES</h2>
  <div class="services-rule"></div>

  <section class="service-card card-residential">
    <h3>RESIDENTIAL</h3>
    <div class="service-photo photo-residential" role="img" aria-label="Two-storey painted family home under a blue sky"></div>
    <p>Lorem ipsum dolor sit amet, consectetuer adipiscing elit, sed diam nonummy nibh euismod tincidunt ut laoreet dolore magna aliquam erat volutpat.</p>
    <a class="read-more" href="#">READ MORE...</a>
  </section>

  <section class="service-card card-commercial">
    <h3>COMMERCIAL</h3>
    <div class="service-photo photo-commercial" role="img" aria-label="Modern white commercial office building with blue glass windows"></div>
    <p>Lorem ipsum dolor sit amet, consectetuer adipiscing elit, sed diam nonummy nibh euismod tincidunt ut laoreet dolore magna aliquam erat volutpat.</p>
    <a class="read-more" href="#">READ MORE...</a>
  </section>

  <section class="service-card card-insurance">
    <h3>INSURANCE</h3>
    <div class="service-photo photo-insurance" role="img" aria-label="Contemporary white house with lawn and blue sky"></div>
    <p>Lorem ipsum dolor sit amet, consectetuer adipiscing elit, sed diam nonummy nibh euismod tincidunt ut laoreet dolore magna aliquam erat volutpat.</p>
    <a class="read-more" href="#">READ MORE...</a>
  </section>

  <footer class="site-footer">
    <div class="member-label">Registered Member</div>
    <div class="member-badge" role="img" aria-label="Guild Decorators Australia member badge"></div>
    <div class="copyright">COPYRIGHT@ 2012</div>
  </footer>
</body>
</html>
```